Covid 19 Exit Strategy one page brochure

I would like to design, and will need URGENT help, a brochure detailing a Covid 19 Exit Strategy plan. This brochure will need to be understood easily and the graphics inside should make it easy for people to understand without reading the entire text. This project is quite urgent and needs to be completed THIS WEEK - by Saturday may 16th at the latest. I am attaching two examples. I will provide the text.

```html
<!DOCTYPE html>
<html lang="en">
<head>
<meta charset="utf-8">
<title>COVID-19 Phased Exit Strategy</title>
<link href="https://fonts.googleapis.com/css2?family=Comfortaa:wght@300;400&family=Poppins:wght@600;700&family=Mulish:wght@400;700&display=swap" rel="stylesheet">
<style>
:root{
  --backdrop:#7b7a85;
  --paper:#ffffff;
  --teal:#0aafd0;
  --red:#c81f36;
  --ink:#1f1f24;
  --white:#ffffff;
}
*{box-sizing:border-box;margin:0;padding:0}
html,body{width:1200px;height:2970px;overflow:hidden;background:var(--backdrop)}
body{font-family:"Mulish",Arial,sans-serif;color:var(--ink)}
.canvas{position:relative;width:1200px;height:2970px;background:var(--backdrop)}
.panel{position:absolute;left:53px;width:1068px}
.panel--intro{top:72px;height:830px;background:var(--paper)}
.panel--stage1{top:902px;height:551px;background:var(--teal)}
.panel--stage1b{top:1499px;height:211px;background:var(--teal)}
.panel--stage2{top:1710px;height:656px;background:var(--paper)}
.panel--stage3{top:2366px;height:513px;background:var(--red)}

.title{position:absolute;left:84px;font-family:"Comfortaa",sans-serif;font-weight:400;color:var(--ink);line-height:1}
.title--main{top:126px;font-size:60px}
.title--sub{top:190px;font-size:49px}
.byline{position:absolute;left:83px;top:255px;width:530px;height:53px;background:var(--teal);color:var(--white);
  font-family:"Comfortaa",sans-serif;font-size:31px;line-height:53px;text-align:center}
.byline strong{font-family:"Poppins",sans-serif;font-weight:700}
.intro{position:absolute;left:84px;top:330px;width:535px;font-size:12.4px;line-height:14.5px;text-align:justify}
.illustration{position:absolute;left:640px;top:161px;width:453px;height:479px;border-radius:48% 52% 40% 45%/40% 45% 55% 52%;
  background:radial-gradient(circle at 20% 20%,#d02a42 0 22%,transparent 23%),linear-gradient(160deg,#10b5d3,#2a4f9a 70%,#6a86c8)}
.rule{position:absolute;left:81px;top:490px;width:63px;height:4px;background:var(--red)}
.section-title{position:absolute;left:81px;top:502px;font-family:"Poppins",sans-serif;font-weight:700;font-size:19.5px}

.item{position:absolute;display:flex;align-items:center;gap:12px;font-size:12.4px;line-height:14.6px}
.icon{flex:none;width:42px;height:42px;border-radius:50%;border:2px solid var(--red);background:var(--white);
  display:flex;align-items:center;justify-content:center}
.icon::after{content:"";width:16px;height:16px;border-radius:4px;background:var(--teal);opacity:.85}
.on-teal .icon{border-color:#0a6f86}
.on-teal .icon::after{background:var(--red)}
.on-red .icon{border-color:#fff}
.on-red .icon::after{background:#1d7fa3}
.on-teal,.on-red{color:var(--white)}

.plan-title{position:absolute;left:53px;width:1068px;top:918px;text-align:center;color:var(--white);
  font-family:"Poppins",sans-serif;font-weight:700;font-size:19px;letter-spacing:.46em}
.stage-bar{position:absolute;left:548px;width:63px;height:4px}
.stage-head{position:absolute;left:53px;width:1068px;text-align:center;font-size:12.4px;line-height:14.8px}
.stage-head h2{font-family:"Poppins",sans-serif;font-weight:700;font-size:20px;line-height:24px}
.stage-head b{font-weight:700}
.stage-head--1{top:980px;color:var(--white)}
.stage-head--2{top:1733px;color:var(--ink)}
.stage-head--2 h2{color:var(--red)}
.stage-head--2 p{max-width:620px;margin:0 auto}
.stage-head--3{top:2398px;color:var(--white)}
</style>
</head>
<body>
<div class="canvas">
  <div class="panel panel--intro"></div>
  <div class="panel panel--stage1"></div>
  <div class="panel panel--stage1b"></div>
  <div class="panel panel--stage2"></div>
  <div class="panel panel--stage3"></div>

  <h1 class="title title--main">COVID-19</h1>
  <p class="title title--sub">Phased Exit Strategy</p>
  <div class="byline">Developed by <strong>LEO MARSDEN</strong></div>
  <p class="intro">Pandemics have, historically, seen their end both medically - via herd immunity or immunizations. And while there are several clinical trials underway for potential Covid-19 vaccines, we are still a long way from deploying an effective vaccine and one that will stand the test of time as the virus changes. Covid-19 pandemic will be considered 'ended' when there are only occasional traces of localized cases that are quickly contained in specific locations., Today and in the absence of an effective vaccine(s) and for the re-opening of the economies and social activities to be successful, it is critical that the following basic conditions be in place before any lockdowns are lifted and before social activities resume:</p>
  <div class="illustration" role="img" aria-label="Illustration of a group of people wearing surgical masks in front of a teal and red blob"></div>

  <div class="rule"></div>
  <h2 class="section-title">GENERAL REQUIREMENTS</h2>

  <div class="item" style="left:83px;top:553px;width:250px"><span class="icon"></span><span>Single digit downward trend of documented cases within the past 14- days.</span></div>
  <div class="item" style="left:374px;top:553px;width:250px"><span class="icon"></span><span>Hospitals and the health care system are capable of treating patients without operating on a crisis mode.</span></div>
  <div class="item" style="left:83px;top:636px;width:250px"><span class="icon"></span><span>Ability to screen and test symptomatic individuals within 24 hours of identification. Increased and sufficient testing capacity, to test at least 50% of all population if necessary within a timeframe of 3 months.</span></div>
  <div class="item" style="left:374px;top:628px;width:250px"><span class="icon"></span><span>Ability to surge ICU capacity on a short notice - 24h.</span></div>
  <div class="item" style="left:374px;top:699px;width:410px"><span class="icon"></span><span>Plan in place to trigger targeted or full-scale containment in case of sudden outbreaks</span></div>
  <div class="item" style="left:841px;top:681px;width:255px"><span class="icon"></span><span>Mandatory daily checks of body temperature for everyone at the workplace or entering public areas.</span></div>
  <div class="item" style="left:86px;top:774px;width:250px"><span class="icon"></span><span>Ability to track and trace infected patients and contacts on a live basis and across the country and ability to react quickly to any unusual trends or outbreaks.</span></div>
  <div class="item" style="left:374px;top:774px;width:440px"><span class="icon"></span><span>Mandatory use of masks (at least surgical grade) for everyone in all public areas and at work. Mandatory use of N95, or equivalent, masks for all healthcare front workers and for all government agencies and authorities that are involved in overseeing the containment activities. 8</span></div>
  <div class="item" style="left:841px;top:774px;width:255px"><span class="icon"></span><span>Mandatory sanitation in all places - use of disinfection available on a large scale.</span></div>

  <h2 class="plan-title">PHASED COVID-19 LOCKDOWN EXIT STRATEGY PLAN</h2>
  <div class="stage-bar" style="top:969px;background:var(--white)"></div>
  <div class="stage-head stage-head--1">
    <h2>STAGE 1</h2>
    <p>To enter this stage, additional to the general requirements, the Effective Reproduction Number (Rt) must be less than 1 and the death rate at less than 3%.</p>
    <p><b>The economy and social activities can resume in this sequence:</b></p>
  </div>

  <div class="on-teal">
    <div class="item" style="left:83px;top:1070px;width:260px"><span class="icon"></span><span>Elderly (60+ years old) and vulnerable individuals should continue to self-isolate.</span></div>
    <div class="item" style="left:83px;top:1131px;width:260px"><span class="icon"></span><span>No more than 5 people maximum gathering at a time in public areas and at work.</span></div>
    <div class="item" style="left:83px;top:1203px;width:260px"><span class="icon"></span><span>Work from home should continue whenever and as much as possible.</span></div>
    <div class="item" style="left:83px;top:1274px;width:260px"><span class="icon"></span><span>Social distancing should continue to be re-enforced in public areas, at work and in all areas reopened.</span></div>
    <div class="item" style="left:83px;top:1356px;width:260px"><span class="icon"></span><span>Non-essential travel should be minimized between cities and regions (and within cities and regions where covid-19 infections are still a risk)</span></div>

    <div class="item" style="left:372px;top:1070px;width:355px"><span class="icon"></span><span>Large businesses (300 people and more, manufacturing, services, etc.) can reopen progressively. Common areas should remain closed (cafeteria, restaurant, gym, meeting rooms of no more than 5 people).</span></div>
    <div class="item" style="left:372px;top:1167px;width:355px"><span class="icon"></span><span>Small businesses (300 people and less) can reopen as well with the same conditions as large businesses.</span></div>
    <div class="item" style="left:372px;top:1236px;width:355px"><span class="icon"></span><span>Commercial shops can reopen. Shops should control the flow of people in their facilities not to exceed 30% at a time of standard capacity. Shops should provide disinfectant and temperature control at entry.</span></div>
    <div class="item" style="left:372px;top:1332px;width:355px"><span class="icon"></span><span>Pharmacies will continue to be open. However, they must make available disinfectant for use by clients and will continue to comply with social distancing. Pharmacies should limit the number of client/patient in their stores not to exceed 30% of the standard capacity.</span></div>

    <div class="item" style="left:747px;top:1070px;width:350px"><span class="icon"></span><span>Transportation (buses, taxis, airlines) will resume progressively. No air travels permitted in and out of Covid-19 known hotspots, locally or internationally. Entry to country should be limited and strictly controlled. All landing passengers and visitors regardless of the country of origin should be tested for Covid-19 at arrival. All passengers and visitors will undergo a temperature check at arrival. No more than 3 people at a time in a taxi/rideshare including the driver. All passengers wearing masks. Buses should operate with no more than 30% customer's capacity per bus.</span></div>
    <div class="item" style="left:758px;top:1322px;width:345px"><span class="icon"></span><span>Religious sites can reopen with a maximum capacity of 30% or less. Social distancing and wearing masks is mandatory. Religious sites should organize (volunteers can help) to check body temperature of everyone accessing the site and provide disinfectant at entry.</span></div>

    <div class="item" style="left:80px;top:1538px;width:470px"><span class="icon"></span><span>Hotels &amp; tourism (museums, etc.) can reopen but must operate at 30% or less capacity. All common areas (restaurants, gyms, swimming pools, conference rooms, etc.) should remain closed.</span></div>
    <div class="item" style="left:612px;top:1538px;width:480px"><span class="icon"></span><span>All schools should remain closed. On-line courses should continue be the preferred method for education</span></div>
    <div class="item" style="left:80px;top:1619px;width:470px"><span class="icon"></span><span>Coffee &amp; restaurants can reopen but must operate at 30% capacity as well and comply with social distancing. Clients must wear as much as possible their masks if they are not consuming food/coffee. Clients should avoid to talking to each other with masks off.</span></div>
    <div class="item" style="left:612px;top:1619px;width:480px"><span class="icon"></span><span>Large scale events (cinema, theaters, sport, business conferences, etc.) should remain closed or operate virtually. Sport events can resume but without spectators. Athletes and the staff surrounding them should be tested, disinfectants should be available and masks used as much as reasonably possible.</span></div>
  </div>

  <div class="stage-bar" style="top:1728px;background:var(--red)"></div>
  <div class="stage-head stage-head--2">
    <h2>STAGE 2</h2>
    <p>To enter this stage, additional to the general requirements, the Effective Reproduction Number (Rt) must be less than 1 and the death rate at less than 3%.</p>
    <p><b>The economy and social activities can resume in this sequence:</b></p>
  </div>

  <div class="item" style="left:83px;top:1822px;width:260px"><span class="icon"></span><span>Elderly (60+ years old) and vulnerable individuals should continue to self-isolate as much as possible. If</span></div>
  <div class="item" style="left:83px;top:1962px;width:260px"><span class="icon"></span><span>No more than 10 people maximum gathering at a time in public areas and at work.</span></div>
  <div class="item" style="left:83px;top:2071px;width:260px"><span class="icon"></span><span>Work from home should if possible or for jobs that do not have to be necessarily in an office setup.</span></div>
  <div class="item" style="left:83px;top:2185px;width:260px"><span class="icon"></span><span>Social distancing can be relaxed. However people should continue to wear masks and use disinfectants</span></div>
  <div class="item" style="left:83px;top:2293px;width:260px"><span class="icon"></span><span>Travel can resume between cities and regions. The same containment restrictions should apply to any existing hotspot.</span></div>

  <div class="item" style="left:359px;top:1822px;width:260px"><span class="icon"></span><span>Elective surgeries can resume in hospitals and clinics that are equipped to comply with all general requirements.</span></div>
  <div class="item" style="left:359px;top:1934px;width:260px"><span class="icon"></span><span>Large businesses (300 people and more, manufacturing, services, etc.) will continue to operate. Common areas should open but social distancing should remain (cafeteria, restaurant, gym, meeting rooms of no more than 10 people).</span></div>
  <div class="item" style="left:359px;top:2089px;width:260px"><span class="icon"></span><span>Small businesses (300 people and less) will continue to operate with the same conditions as large businesses. i</span></div>
  <div class="item" style="left:359px;top:2194px;width:260px"><span class="icon"></span><span>Commercial shops will continue to be open and can operate at 50% capacity. Wear of masks should continue.</span></div>
  <div class="item" style="left:359px;top:2293px;width:260px"><span class="icon"></span><span>Pharmacies will continue to be open and will need to operate a 50% capacity k</span></div>

  <div class="item" style="left:660px;top:1822px;width:430px"><span class="icon"></span><span>Transportation (buses, taxis, and airlines) will continue to operate. Still no air travels permitted in and out of Covid-19 known hotspots, locally or internationally. Entry to country should be relaxed but remain controlled. Airports should continue to use thermo cameras to monitor passenger's temperature at landing. Airports should be equipped to test for Covid-19 if necessary. Transportation by taxi/rideshare continues, however, passengers wear masks. Buses could operate with 50% capacity per bus.</span></div>
  <div class="item" style="left:660px;top:1975px;width:430px"><span class="icon"></span><span>Religious sites can operate with a maximum capacity of 50%. Social distancing and wearing masks should be enforced. Sites should continue to check body temperature of everyone accessing the site and provide disinfectant at entry.</span></div>
  <div class="item" style="left:660px;top:2058px;width:430px"><span class="icon"></span><span>Hotels &amp; tourism (museums, etc.) can operate at 50% capacity. All common areas (restaurants, gyms, swimming pools, conference rooms, etc.) could reopen. Gatherings are limited to 10 people or less and can be expanded with social distancing and wearing protective masks.</span></div>
  <div class="item" style="left:660px;top:2148px;width:430px"><span class="icon"></span><span>Coffee &amp; restaurants can operate at 50% capacity and continue comply with social distancing. Clients must wear as much as possible their masks if they are not consuming food/coffee.</span></div>
  <div class="item" style="left:660px;top:2229px;width:430px"><span class="icon"></span><span>Schools can reopen in parallel with on-line education. Social distancing and re-arranging school seating to prevent the spread of infection is mandatory</span></div>
  <div class="item" style="left:660px;top:2293px;width:430px"><span class="icon"></span><span>Large scale events (cinema, theaters, sport, business conferences, etc.) could resume under strict social distancing. People should wear masks.</span></div>

  <div class="stage-bar" style="top:2394px;background:var(--white)"></div>
  <div class="stage-head stage-head--3">
    <h2>STAGE 3</h2>
    <p>To enter stage 3 of the Covid-19 Exit Strategy, compliance to the general requirements is compulsory, additional to a successful Stage 2 outcome.<br>The Effective Reproduction Number (Rt) for Stage 3 must be less than 0.3 and the death rate stabilized at less than 1%.</p>
    <p><b>The economy and social activities can resume in this sequence:</b></p>
  </div>

  <div class="on-red">
    <div class="item" style="left:83px;top:2486px;width:342px"><span class="icon"></span><span>Elderly (60+ years old) and vulnerable individuals may resume all previously exercised activities without restrictions. Restrictions as to the number of people gathering together can be lifted. Social distancing can be relaxed. However, wear of masks may continue.</span></div>
    <div class="item" style="left:83px;top:2609px;width:342px"><span class="icon"></span><span>Travel can resume between cities and regions and out of country travel. The same containment restrictions as Stage 1 and 2 would continue to apply to any existing hotspot</span></div>
    <div class="item" style="left:83px;top:2707px;width:342px"><span class="icon"></span><span>All hospital and clinic surgeries can resume in hospitals in compliance with standard hospital and health care procedures.</span></div>
    <div class="item" style="left:83px;top:2798px;width:342px"><span class="icon"></span><span>Large businesses (300 people and more, manufacturing, services, etc.) will resume normal business practices. Wear of masks is recommended but not mandatory.</span></div>

    <div class="item" style="left:440px;top:2487px;width:350px"><span class="icon"></span><span>Small businesses (300 people and less) will operate with the same conditions as large businesses.</span></div>
    <div class="item" style="left:440px;top:2558px;width:350px"><span class="icon"></span><span>Commercial shops can operate on a normal mode - previous to covid- 19. Wear of masks could be recommended in certain areas</span></div>
    <div class="item" style="left:440px;top:2636px;width:350px"><span class="icon"></span><span>Pharmacies can operate at a normal state.</span></div>
    <div class="item" style="left:440px;top:2690px;width:350px"><span class="icon"></span><span>Transportation (buses, taxis, and airlines) will operate at a normal capacity. Still no air travels permitted in and out of Covid-19 known hotspots, locally or internationally. Entry to country should be relaxed and operate normally. Airports should continue to use thermo cameras to monitor passenger's temperature at landing. Airports should be equipped to test for Covid-19 if necessary. Transportation by taxi/rideshare and buses will resume on a normal mode. Wear of masks is elective.</span></div>

    <div class="item" style="left:805px;top:2477px;width:290px"><span class="icon"></span><span>Religious sites can operate normally. Wear of masks should be elective</span></div>
    <div class="item" style="left:805px;top:2549px;width:290px"><span class="icon"></span><span>Hotels &amp; tourism (museums, etc.) can operate at 100% capacity including all common areas</span></div>
    <div class="item" style="left:805px;top:2629px;width:290px"><span class="icon"></span><span>Coffee &amp; restaurants can resume normal operations. Clients may wear masks for personal protection if they wish to.</span></div>
    <div class="item" style="left:805px;top:2713px;width:290px"><span class="icon"></span><span>Schools can resume operations. Re-arranging school seating should continue until a vaccine is found.</span></div>
    <div class="item" style="left:805px;top:2785px;width:290px"><span class="icon"></span><span>Large scale events (cinema, theaters, sport, business conferences, etc.) could resume under moderate social distancing. People may elect to wear masks.</span></div>
  </div>
</div>
</body>
</html>
```